Full service meeting planning company needs new business cards

Bright Harbor is a full service meeting planning company that specializes in on-line conference registration web development and event communications. We combine citywide hotel management, mobile applications, eblast reminders, confirmation letters, and customized reporting to create a seamless registration process. We also manage group motor coach transportation, food and beverages, entertainment, stage and lighting for group of 10 to 4000.

Target Market(s)

Corporations and associations

Industry/Entity Type

Event Planning

Contact Information for Business Card

standard size 3.5" wide and 2" tall

Font styles to use
Serif
Sans Serif

Colors
f37122
f78f20
333333
5c5c5c
9d9d9d
f68d4d

Requirements
Must have
• {name}
• Bright Harbor
• P.O. Box 7384, Grand Rapids, M I 49577
• www.brightharborplan.com
• {email}
• {phone}
• {mobile phone}
Nice to have
• Our colors are black, grey and orange as an accent color
Should not have
• I am not happy with our website layout anymore either. It feels dark and old but it does explain who we are pretty well if you'd like to review; www.brightharborplan.com

```html
<!DOCTYPE html>
<html lang="en">
<head>
<meta charset="utf-8">
<title>Bright Harbor Business Card</title>
<link rel="stylesheet" href="https://fonts.googleapis.com/css2?family=Source+Sans+3:wght@400;600&display=swap">
<style>
  :root {
    --stage: #000000;
    --card: #38383b;
    --card-edge: #3f3f42;
    --ink: #bfbfbf;
    --ink-soft: #a9a9a9;
    --mark: #9d9d9d;
    --rule: #2e2e31;
  }
  html, body {
    margin: 0;
    width: 1200px;
    height: 900px;
    overflow: hidden;
    background: var(--stage);
    font-family: "Source Sans 3", "Myriad Pro", Arial, sans-serif;
  }
  .card {
    position: absolute;
    top: 271px;
    width: 456px;
    height: 281px;
    border-radius: 12px;
    background: linear-gradient(180deg, var(--card-edge), var(--card));
  }
  .card--front { left: 137px; }
  .card--back { left: 627px; }

  .front-brand {
    position: absolute;
    left: 0;
    top: 0;
    width: 196px;
    height: 281px;
    display: flex;
    flex-direction: column;
    align-items: center;
    justify-content: center;
    gap: 12px;
  }
  .brand-dot {
    width: 70px;
    height: 70px;
    border-radius: 50%;
    background: var(--mark);
  }
  .brand-name {
    color: var(--mark);
    font-size: 17px;
    font-weight: 600;
    letter-spacing: 0.02em;
  }
  .divider {
    position: absolute;
    left: 196px;
    top: 22px;
    width: 1px;
    height: 236px;
    background: linear-gradient(180deg, transparent, var(--rule) 20%, var(--rule) 80%, transparent);
  }

  .details {
    position: absolute;
    left: 237px;
    top: 58px;
    color: var(--ink-soft);
  }
  .person-name {
    margin: 0;
    color: var(--ink);
    font-size: 17px;
    font-weight: 600;
    line-height: 22px;
  }
  .person-role {
    margin: 0;
    font-size: 13px;
    line-height: 16px;
  }
  .address {
    margin: 14px 0 0;
    font-size: 13px;
    line-height: 14px;
    font-style: normal;
  }
  .contact-list {
    list-style: none;
    margin: 15px 0 0;
    padding: 0;
    font-size: 13px;
    line-height: 19px;
  }
  .contact-list li {
    display: flex;
    align-items: center;
    gap: 8px;
  }
  .contact-list svg {
    width: 9px;
    height: 9px;
    fill: var(--ink-soft);
    flex: none;
  }

  .back-brand {
    position: absolute;
    inset: 0;
    display: flex;
    flex-direction: column;
    align-items: center;
    justify-content: center;
    gap: 10px;
    padding-top: 14px;
    box-sizing: border-box;
  }
  .back-brand .brand-dot {
    width: 106px;
    height: 106px;
  }
  .back-brand .brand-name {
    font-size: 21px;
    letter-spacing: 0.03em;
    text-transform: uppercase;
  }
</style>
</head>
<body>

<section class="card card--front" aria-label="Card front">
  <div class="front-brand">
    <div class="brand-dot"></div>
    <span class="brand-name">Bright Harbor</span>
  </div>
  <div class="divider"></div>
  <div class="details">
    <p class="person-name">Marcus Ellery</p>
    <p class="person-role">Managing Director</p>
    <address class="address">P.O. Box 7384, Grand<br>Rapids, M I 49577</address>
    <ul class="contact-list">
      <li>
        <svg viewBox="0 0 10 10" aria-hidden="true"><path d="M2 0.5 L3.6 2.6 L2.8 3.8 Q4 6 6.2 7.2 L7.4 6.4 L9.5 8 L8.4 9.5 Q4.5 9.5 2 7 Q0.5 5 0.5 1.6 Z"/></svg>
        <span>(616)-555-0142</span>
      </li>
      <li>
        <svg viewBox="0 0 10 10" aria-hidden="true"><path d="M2.5 0 H7.5 V10 H2.5 Z M3.5 1 V8 H6.5 V1 Z" fill-rule="evenodd"/></svg>
        <span>616-555-0187</span>
      </li>
      <li>
        <svg viewBox="0 0 10 10" aria-hidden="true"><path d="M0.5 2 H9.5 V8.5 H0.5 Z"/><path d="M0.5 2 L5 5.5 L9.5 2" fill="none" stroke="#38383b" stroke-width="0.9"/></svg>
        <span>hello@brightharborplan.com</span>
      </li>
      <li>
        <svg viewBox="0 0 10 10" aria-hidden="true"><circle cx="5" cy="5" r="4.6"/></svg>
        <span>www.brightharborplan.com</span>
      </li>
    </ul>
  </div>
</section>

<section class="card card--back" aria-label="Card back">
  <div class="back-brand">
    <div class="brand-dot"></div>
    <span class="brand-name">Bright Harbor</span>
  </div>
</section>

</body>
</html>
```